Frost Harbor Supply Inc. Box Truck Wrap

I'm looking for design ideas for wrapping my box truck using any of these photos or ideas you may have. Nothing too colorful but more professional. We are looking to target ice cream shop owners and not children as we are just a delivery truck. Nothing too cartoonish. Please feel free to use any of the photos I have uploaded or if you have a better idea you are welcome to give that a shot.
Updates

Target Market(s)

Small business like ice cream shops

Industry/Entity Type

Ice Cream product wholesale distributor

Requirements
Must have
• our logo, phone #: 856-719-2264, website: www.frostharborsupplyinc.example, email: sales@frostharborsupplyinc.example, product categories we carry. (Ice Cream, Mixes, Syrups/Bases, Topping, Cones, Water Ice )
Nice to have
• Pictures of the products
Should not have
• not too colorful. more professional

```html
<!DOCTYPE html>
<html lang="en">
<head>
<meta charset="utf-8">
<title>Frost Harbor Supply Inc. – Box Truck Wrap</title>
<link rel="stylesheet" href="https://fonts.googleapis.com/css2?family=Josefin+Sans:wght@400;600;700&display=swap">
<style>
  :root {
    --salmon: #fa8474;
    --white: #ffffff;
    --frame: #3a3a3a;
    --chassis: #333333;
    --tire: #222222;
    --rim: #c4c4c4;
    --steel: #d2d2d2;
    --cream: #e8d3b4;
    --cocoa: #8a5a3c;
    --mint: #a9d3b8;
    --berry: #e9a6b4;
    --amber: #f08a2c;
    --signal: #c8322c;
    --font: "Josefin Sans", sans-serif;
  }
  * { box-sizing: border-box; margin: 0; padding: 0; }
  html, body { width: 1200px; height: 923px; overflow: hidden; background: var(--white); }
  .canvas { position: relative; width: 1200px; height: 923px; font-family: var(--font); color: var(--white); }
  .vehicle-art { position: absolute; left: 0; top: 0; width: 1200px; height: 923px; }

  /* cargo box side panel */
  .box-panel {
    position: absolute; width: 485px; height: 247px;
    background: var(--salmon); border: 4px solid var(--frame); border-radius: 5px; overflow: hidden;
  }
  .box-panel .category-band {
    position: absolute; left: 6px; right: 6px; top: 4px; height: 38px; background: var(--white);
    border-radius: 0 0 40% 60% / 0 0 18px 12px;
    color: var(--salmon); font-size: 14.5px; text-align: center; padding-top: 10px; letter-spacing: .3px; white-space: nowrap;
  }
  .box-panel .sprinkles {
    position: absolute; left: 8px; right: 8px; top: 44px; height: 26px;
    background: linear-gradient(90deg, rgba(255,255,255,0), rgba(255,255,255,.18), rgba(255,255,255,0));
    border-radius: 4px;
  }
  .box-panel .cone-art {
    position: absolute; width: 108px; height: 112px; top: 50px;
    background: linear-gradient(160deg, rgba(255,255,255,.22), rgba(255,255,255,.08)); border-radius: 6px;
  }
  .box-panel .scoop-strip {
    position: absolute; left: 0; right: 0; top: 160px; height: 46px;
    background: linear-gradient(90deg, var(--mint), var(--cocoa) 14%, var(--cream) 28%, var(--berry) 42%, var(--cocoa) 55%, var(--cream) 68%, var(--mint) 80%, var(--berry) 90%, var(--cream));
  }
  .box-panel .contact-band {
    position: absolute; left: 6px; right: 6px; top: 206px; height: 22px; background: var(--white);
    display: flex; justify-content: space-between; align-items: center; padding: 3px 44px 0 14px;
    color: var(--salmon);
  }
  .contact-band .web { font-size: 14.5px; letter-spacing: .3px; }
  .contact-band .phone { font-size: 18px; }
  .brand { position: absolute; white-space: nowrap; }
  .brand .name { display: block; font-weight: 700; font-size: 20.5px; letter-spacing: .2px; }
  .brand .tagline { display: block; font-size: 15.5px; letter-spacing: 3.4px; margin-top: 4px; padding-left: 3px; }

  /* cab door lettering */
  .door-brand { position: absolute; text-align: center; white-space: nowrap; line-height: 1.25; }
  .door-brand .name { font-size: 6px; font-weight: 700; display: block; }
  .door-brand .tagline { font-size: 4.5px; letter-spacing: 1px; display: block; }
  .door-brand .phone { font-size: 7px; display: block; }
  .door-brand .email { font-size: 4px; display: block; }

  /* front view */
  .front-box { position: absolute; left: 904px; top: 65px; width: 214px; height: 98px; background: var(--salmon); border: 4px solid var(--frame); border-bottom: none; border-radius: 4px 4px 0 0; }
  .front-box .brand { left: 50px; top: 42px; }
  .front-box .brand .name { font-size: 9.5px; }
  .front-box .brand .tagline { font-size: 7.5px; letter-spacing: 1.4px; margin-top: 1px; }
  .front-email { position: absolute; left: 905px; width: 213px; top: 272px; text-align: center; font-size: 7.5px; }

  /* rear view */
  .rear-doors { position: absolute; left: 904px; top: 517px; width: 214px; height: 245px; background: var(--salmon); border: 4px solid var(--frame); border-radius: 4px; }
  .rear-doors .seam { position: absolute; top: 0; bottom: 0; width: 4px; border-left: 1px solid var(--white); border-right: 1px solid var(--white); }
  .rear-doors .web { position: absolute; top: 20px; left: 0; right: 0; text-align: center; font-size: 11px; }
  .rear-doors .cone-art { position: absolute; left: 62px; top: 45px; width: 90px; height: 100px; background: rgba(255,255,255,.15); border-radius: 6px; }
  .rear-doors .door-brand.left { left: 12px; top: 160px; text-align: left; }
  .rear-doors .door-brand.left .name { font-size: 5.5px; }
  .rear-doors .door-brand.right { left: 120px; top: 161px; text-align: left; }
  .rear-doors .door-brand.right .phone { font-size: 12px; }
  .rear-doors .door-brand.right .email { font-size: 4.2px; }
</style>
</head>
<body>
<main class="canvas">

  <svg class="vehicle-art" viewBox="0 0 1200 923" aria-hidden="true">
    <defs>
      <g id="wheel">
        <circle r="38" fill="var(--tire)"/>
        <circle r="23" fill="var(--rim)" stroke="#8a8a8a" stroke-width="1.5"/>
        <circle r="7" fill="none" stroke="#555" stroke-width="1.2"/>
      </g>
      <!-- side chassis and cab, nose facing right -->
      <g id="truck-side">
        <!-- frame under box -->
        <rect x="62" y="311" width="487" height="36" fill="var(--chassis)"/>
        <path d="M62 330 L90 318 L90 342 L62 352 Z" fill="var(--chassis)"/>
        <rect x="62" y="326" width="6" height="28" fill="var(--chassis)"/>
        <path d="M190 318 Q246 300 300 318 L300 360 L190 360 Z" fill="var(--chassis)"/>
        <rect x="300" y="330" width="245" height="5" fill="var(--steel)" stroke="#888" stroke-width=".6"/>
        <rect x="300" y="351" width="245" height="5" fill="var(--steel)" stroke="#888" stroke-width=".6"/>
        <rect x="418" y="319" width="66" height="12" fill="var(--steel)" stroke="#888" stroke-width=".6"/>
        <rect x="156" y="324" width="10" height="18" rx="2" fill="#222"/>
        <!-- cab body -->
        <path d="M547 161 L610 163 Q640 166 650 178 L708 237 Q730 262 775 276 Q795 282 798 300 L802 340 L805 354 Q804 366 790 368 L547 368 Z" fill="var(--salmon)" stroke="var(--frame)" stroke-width="1.4"/>
        <!-- lower dark band with wheel arch -->
        <path d="M547 316 L805 316 L805 354 Q804 366 790 368 L748 368 A47 47 0 0 0 654 368 L547 368 Z" fill="var(--chassis)"/>
        <path d="M565 316 L565 352 Q566 360 575 360 L670 360 L670 316" fill="none" stroke="var(--frame)" stroke-width="1"/>
        <!-- door outline -->
        <path d="M561 172 L606 172 L676 248 L672 316 L561 316 Z" fill="none" stroke="var(--frame)" stroke-width="1"/>
        <!-- side window -->
        <path d="M570 180 Q566 184 567 192 L574 240 Q576 246 584 247 L690 256 L612 183 Q608 180 600 180 Z" fill="var(--white)" stroke="var(--frame)" stroke-width="1.2"/>
        <line x1="625" y1="192" x2="629" y2="250" stroke="var(--frame)" stroke-width="1"/>
        <!-- windshield edge -->
        <path d="M636 170 L710 234 L703 238 L630 172 Z" fill="var(--white)" stroke="var(--frame)" stroke-width="1"/>
        <!-- mirror -->
        <rect x="647" y="224" width="10" height="26" rx="3" fill="var(--chassis)"/>
        <!-- handle -->
        <rect x="570" y="263" width="28" height="4" rx="2" fill="var(--chassis)"/>
        <!-- headlight -->
        <path d="M750 284 Q770 276 790 286 L796 306 Q778 310 752 296 Z" fill="var(--white)" stroke="var(--frame)" stroke-width="1.2"/>
        <circle cx="782" cy="340" r="4" fill="#bbb" stroke="#222"/>
        <!-- wheels -->
        <use href="#wheel" x="246" y="357"/>
        <use href="#wheel" x="701" y="357"/>
      </g>
    </defs>

    <use href="#truck-side"/>
    <use href="#truck-side" transform="translate(865 452) scale(-1 1)"/>

    <!-- front view -->
    <rect x="908" y="362" width="28" height="33" rx="3" fill="var(--tire)"/>
    <rect x="1087" y="362" width="28" height="33" rx="3" fill="var(--tire)"/>
    <path d="M920 166 L1102 166 Q1112 168 1113 180 L1118 290 L1118 368 Q1118 374 1110 374 L912 374 Q905 374 905 368 L905 290 L910 180 Q911 168 920 166 Z" fill="var(--salmon)" stroke="var(--frame)" stroke-width="1.4"/>
    <path d="M905 316 L1118 316 L1118 368 Q1118 374 1110 374 L912 374 Q905 374 905 368 Z" fill="var(--chassis)"/>
    <path d="M924 177 L1098 177 Q1104 177 1104 184 L1108 246 L916 248 L919 184 Q919 177 924 177 Z" fill="var(--white)" stroke="var(--frame)" stroke-width="1.5"/>
    <rect x="877" y="226" width="22" height="28" rx="6" fill="var(--tire)"/>
    <rect x="1124" y="226" width="22" height="28" rx="6" fill="var(--tire)"/>
    <path d="M912 284 Q930 276 946 290 L944 312 Q925 314 912 302 Z" fill="var(--white)" stroke="var(--frame)" stroke-width="1.2"/>
    <path d="M1111 284 Q1093 276 1077 290 L1079 312 Q1098 314 1111 302 Z" fill="var(--white)" stroke="var(--frame)" stroke-width="1.2"/>
    <circle cx="915" cy="288" r="4" fill="var(--amber)"/>
    <circle cx="1108" cy="288" r="4" fill="var(--amber)"/>
    <path d="M946 290 Q1011 276 1077 290 L1070 318 Q1011 330 953 318 Z" fill="#ddd" stroke="#555" stroke-width="1.2"/>
    <g stroke="#777" stroke-width=".8">
      <line x1="956" y1="296" x2="1067" y2="296"/><line x1="954" y1="301" x2="1069" y2="301"/>
      <line x1="955" y1="306" x2="1068" y2="306"/><line x1="957" y1="311" x2="1066" y2="311"/>
    </g>
    <path d="M975 332 L1048 332 L1056 352 L967 352 Z" fill="#2a2a2a"/>
    <circle cx="930" cy="341" r="5" fill="#ccc"/><circle cx="1093" cy="341" r="5" fill="#ccc"/>

    <!-- rear view -->
    <rect x="880" y="678" width="20" height="28" rx="6" fill="var(--rim)" stroke="var(--tire)" stroke-width="2"/>
    <rect x="1122" y="678" width="20" height="28" rx="6" fill="var(--rim)" stroke="var(--tire)" stroke-width="2"/>
    <rect x="908" y="762" width="206" height="52" fill="var(--chassis)"/>
    <rect x="906" y="780" width="210" height="24" fill="#444" stroke="#222"/>
    <g>
      <rect x="908" y="782" width="11" height="20" fill="var(--signal)"/><rect x="920" y="782" width="11" height="20" fill="var(--white)"/>
      <rect x="932" y="782" width="11" height="20" fill="var(--signal)"/><rect x="944" y="782" width="11" height="20" fill="var(--amber)"/>
      <rect x="1067" y="782" width="11" height="20" fill="var(--signal)"/><rect x="1079" y="782" width="11" height="20" fill="var(--white)"/>
      <rect x="1091" y="782" width="11" height="20" fill="var(--signal)"/><rect x="1103" y="782" width="11" height="20" fill="var(--amber)"/>
    </g>
    <rect x="908" y="812" width="24" height="36" rx="2" fill="var(--tire)"/>
    <rect x="935" y="812" width="24" height="36" rx="2" fill="var(--tire)"/>
    <rect x="1063" y="812" width="24" height="36" rx="2" fill="var(--tire)"/>
    <rect x="1090" y="812" width="24" height="36" rx="2" fill="var(--tire)"/>
    <path d="M960 812 Q1011 830 1062 812 Z" fill="var(--chassis)"/>
  </svg>

  <!-- Passenger side -->
  <section class="box-panel" style="left:59px; top:64px;">
    <div class="category-band">Ice Cream • Mixes • Syrups/Bases • Topping • Cones • Water Ice</div>
    <div class="sprinkles" role="img" aria-label="Scattered colourful sprinkles"></div>
    <div class="cone-art" style="left:17px;" role="img" aria-label="White line drawings of two waffle cones"></div>
    <div class="scoop-strip" role="img" aria-label="Photo of a row of ice cream scoops in assorted flavours"></div>
    <div class="brand" style="left:219px; top:98px;">
      <span class="name">Frost Harbor Supply Inc.</span>
      <span class="tagline">Wholesale Distributor</span>
    </div>
    <div class="contact-band"><span class="web">www.frostharborsupplyinc.example</span><span class="phone">856-719-2264</span></div>
  </section>
  <div class="door-brand" style="left:583px; top:278px;">
    <span class="name">Frost Harbor Supply Inc.</span>
    <span class="tagline">Wholesale Distributor</span>
    <span class="phone">856-719-2264</span>
    <span class="email">sales@frostharborsupplyinc.example</span>
  </div>
  <div role="img" aria-label="White line drawings of two waffle cones" style="position:absolute; left:685px; top:262px; width:52px; height:42px; background:rgba(255,255,255,.15); border-radius:4px;"></div>

  <!-- Front -->
  <section class="front-box">
    <div class="brand"><span class="name">Frost Harbor Supply Inc.</span><span class="tagline">Wholesale Distributor</span></div>
  </section>
  <div class="front-email">sales@frostharborsupplyinc.example</div>

  <!-- Driver side -->
  <section class="box-panel" style="left:321px; top:517px;">
    <div class="category-band">Ice Cream • Mixes • Syrups/Bases • Topping • Cones • Water Ice</div>
    <div class="sprinkles" role="img" aria-label="Scattered colourful sprinkles"></div>
    <div class="cone-art" style="left:358px;" role="img" aria-label="White line drawings of two waffle cones"></div>
    <div class="scoop-strip" role="img" aria-label="Photo of a row of ice cream scoops in assorted flavours"></div>
    <div class="brand" style="left:76px; top:98px;">
      <span class="name">Frost Harbor Supply Inc.</span>
      <span class="tagline">Wholesale Distributor</span>
    </div>
    <div class="contact-band"><span class="web">www.frostharborsupplyinc.example</span><span class="phone">856-719-2264</span></div>
  </section>
  <div class="door-brand" style="left:208px; top:730px;">
    <span class="name">Frost Harbor Supply Inc.</span>
    <span class="tagline">Wholesale Distributor</span>
    <span class="phone">856-719-2264</span>
    <span class="email">sales@frostharborsupplyinc.example</span>
  </div>
  <div role="img" aria-label="White line drawings of two waffle cones" style="position:absolute; left:124px; top:713px; width:52px; height:42px; background:rgba(255,255,255,.15); border-radius:4px;"></div>

  <!-- Rear -->
  <section class="rear-doors">
    <div class="seam" style="left:90px;"></div>
    <div class="seam" style="left:116px;"></div>
    <div class="web">www.frostharborsupplyinc.example</div>
    <div class="cone-art" role="img" aria-label="White line drawings of two waffle cones"></div>
    <div class="door-brand left">
      <span class="name">Frost Harbor Supply Inc.</span>
      <span class="tagline">Wholesale Distributor</span>
    </div>
    <div class="door-brand right">
      <span class="phone">856-719-2264</span>
      <span class="email">sales@frostharborsupplyinc.example</span>
    </div>
  </section>

</main>
</body>
</html>
```